Upgrade Existing Web Design for an Investments Firm

We need a web designer for a company based in Dubai called Harborline Capital. We have an existing website which needs certain additions and changes. The design should be similar to typical corporate finance company websites. We're providing you with the link of our current website below - http://harborlinegroup.ae/
We would require the mock-ups to be ready in c. 7 working days and another 7 working days for the coding implementation. Timeline and promp response is very important for us as a client.

Target Market(s)

Investors/Consumer Brands/Financial Service Institutions/ Job Seekers

Industry/Entity Type

Financial Service

Coding

Coded - Design and coding required

Number of Pages Required

5+ page

Font styles to use
Other font styles liked:
• Arial

Colors
f04a51
000000
919191
cbcbcb

Requirements
Nice to have
• It should be similar to https://www.tovrenholdings.com
• Mobile Optimised as well

```html
<!DOCTYPE html>
<html lang="en">
<head>
<meta charset="utf-8">
<title>Harborline Partners &amp; Co</title>
<link rel="stylesheet" href="https://fonts.googleapis.com/css2?family=Open+Sans:wght@400;600;700;800&display=swap">
<style>
:root{
  --red:#f04a51;
  --black:#000000;
  --ink:#222222;
  --grey:#919191;
  --light:#cbcbcb;
  --dark:#1c1c1c;
  --darker:#141414;
  --paper:#ffffff;
  --mist:#f3f3f3;
  --sky1:#2a63a6;
  --sky2:#9cc3e8;
}
*{box-sizing:border-box;margin:0;padding:0}
html,body{width:1200px;height:4110px;overflow:hidden}
body{font-family:"Open Sans",Arial,sans-serif;color:var(--ink);background:var(--paper);position:relative}
.abs{position:absolute}

/* header */
.site-header{position:absolute;left:0;top:0;width:1200px;height:95px;background:linear-gradient(#151515,#262626);z-index:2}
.brand{position:absolute;left:96px;top:30px;display:flex;align-items:center;gap:12px;color:#fff;font-weight:700;font-size:24px;letter-spacing:1px}
.brand-square{width:26px;height:26px;background:var(--red)}
.main-nav{position:absolute;right:98px;top:36px;display:flex;gap:42px}
.main-nav a{color:#fff;font-size:13px;font-weight:600;text-decoration:none;letter-spacing:.3px}
.main-nav a.active{color:var(--red)}

/* hero */
.hero{position:absolute;left:0;top:95px;width:1200px;height:467px;background:linear-gradient(160deg,var(--sky2) 0%,#5f95cf 45%,var(--sky1) 100%)}
.hero-title{position:absolute;left:0;width:1200px;text-align:center;color:#fff;text-shadow:0 3px 8px rgba(0,0,0,.35)}
.hero-title.big{top:138px;font-size:86px;font-weight:800;letter-spacing:3px}
.hero-title.small{top:250px;font-size:40px;font-weight:700;letter-spacing:2px}
.hero-dots{position:absolute;top:410px;left:0;width:1200px;display:flex;justify-content:center;gap:8px}
.hero-dots span{width:12px;height:12px;border-radius:50%;border:2px solid #fff}
.hero-dots span.on{background:#fff}

/* section headings */
.section-title{position:absolute;left:0;width:1200px;display:flex;justify-content:center;align-items:center;gap:14px;font-size:26px;font-weight:600;color:var(--ink);text-transform:uppercase}
.section-title .mark{width:22px;height:22px;background:var(--red)}
.section-title em{font-style:normal;color:var(--red)}

/* services */
.service-card{position:absolute;top:726px;width:232px;height:280px;border:1px solid #e2e2e2;text-align:center;padding:0 18px}
.service-card.current{border-bottom:4px solid var(--red)}
.service-card svg{margin-top:32px}
.service-card h3{font-size:15px;font-weight:600;margin-top:16px;line-height:1.45;text-transform:uppercase}
.service-card p{font-size:12px;color:#555;line-height:1.8;margin-top:14px}

/* why */
.why{position:absolute;left:0;top:1096px;width:1200px;height:534px;background:linear-gradient(200deg,#bcd4ee 0%,#5288c4 50%,#1d4f8c 100%)}
.why-red{position:absolute;left:0;top:0}
.why-list{position:absolute;left:164px;top:82px;list-style:none}
.why-list li{display:flex;align-items:center;gap:22px;color:#fff;font-size:15px;font-weight:700;height:58px;text-transform:uppercase}
.why-list li::before{content:"";width:11px;height:11px;border:3px solid #fff;border-radius:50%}
.why-heading{position:absolute;left:560px;width:560px;top:160px;text-align:center;color:#fff;font-size:52px;font-weight:800;line-height:1.25;text-shadow:0 3px 8px rgba(0,0,0,.4)}

/* about */
.about-title{position:absolute;left:96px;top:1725px;display:flex;align-items:center;gap:14px;font-size:26px;font-weight:600;text-transform:uppercase}
.about-title .mark{width:22px;height:22px;background:var(--red)}
.about-title em{font-style:normal;color:var(--red)}
.about-text{position:absolute;left:96px;top:1788px;width:500px;font-size:12.5px;line-height:2.05;color:#555}
.about-text p+p{margin-top:14px}
.btn{display:inline-block;background:var(--red);color:#fff;font-size:13px;font-weight:700;padding:14px 26px;text-transform:uppercase}
.about-photo{position:absolute;left:644px;top:1721px;width:452px;height:389px;background:linear-gradient(135deg,#d7d7d7,#f4f4f4 40%,#8e8e8e);box-shadow:0 6px 16px rgba(0,0,0,.25)}

/* stages */
.stages{position:absolute;left:0;top:2192px;width:1200px;height:562px;background:linear-gradient(135deg,#f7f7f7,#ececec)}
.stage-label{position:absolute;font-size:16px;font-weight:600;color:#222;text-align:center;line-height:1.6}
.stage-notes{position:absolute;left:603px;top:2530px;width:490px;list-style:none}
.stage-notes li{position:relative;padding-left:22px;font-size:12px;line-height:1.9;color:#555;margin-bottom:10px}
.stage-notes li::before{content:"";position:absolute;left:0;top:7px;width:8px;height:8px;border:2px solid var(--red);border-radius:50%}

/* blog */
.post{position:absolute;top:2926px;width:481px}
.post-image{height:252px}
.post h4{margin-top:44px;font-size:16px;font-weight:600;text-transform:uppercase;color:#222}
.post p{margin-top:12px;font-size:12.5px;line-height:1.9;color:#555}
.read-more{display:inline-flex;align-items:center;gap:6px;margin-top:16px;color:var(--red);font-size:13px;font-weight:600}

/* partners */
.partners{position:absolute;left:0;top:3452px;width:1200px;height:206px;display:flex;justify-content:center;align-items:center;gap:88px}
.partner{width:100px;height:56px;border-radius:6px;background:#e7e7e7}

/* footer */
.site-footer{position:absolute;left:0;top:3658px;width:1200px;height:397px;background:var(--dark);border-top:4px solid var(--red);color:#fff}
.footer-col{position:absolute;top:88px}
.footer-col h5{font-size:19px;font-weight:600;margin-bottom:26px}
.contact-line{display:flex;gap:18px;font-size:12px;line-height:1.7;margin-bottom:24px;color:#ddd}
.links{list-style:none}
.links li{display:flex;align-items:center;gap:26px;font-size:12px;color:#ddd;height:33px}
.links li::before{content:"";border-left:7px solid #fff;border-top:5px solid transparent;border-bottom:5px solid transparent}
.newsletter p{font-size:12px;color:#ddd;line-height:1.7;width:260px}
.newsletter .field{margin-top:20px;width:260px;height:42px;background:#fff;color:#888;font-size:12px;padding:13px 14px}
.newsletter .btn{margin-top:14px;padding:11px 22px;font-size:12px}
.copyright{position:absolute;left:0;top:4055px;width:1200px;height:55px;background:var(--darker);color:#bbb;font-size:12px;text-align:center;line-height:55px}
</style>
</head>
<body>

<header class="site-header">
  <div class="brand"><span class="brand-square"></span>HARBORLINE</div>
  <nav class="main-nav">
    <a class="active">HOME</a><a>ABOUT US</a><a>OUR APPROACH</a><a>OUR PORTFOLIO</a><a>OUR PEOPLE</a><a>CONTACT</a>
  </nav>
</header>

<section class="hero" role="img" aria-label="Glass office towers rising into a blue sky">
  <div class="hero-title big">HARBORLINE</div>
  <div class="hero-title small">PARTNERS &amp; CO</div>
  <div class="hero-dots"><span class="on"></span><span></span><span></span><span></span><span></span></div>
</section>

<h2 class="section-title" style="top:638px"><span class="mark"></span>Our Services</h2>

<div class="service-card current" style="left:101px">
  <svg width="62" height="62" viewBox="0 0 62 62"><circle cx="31" cy="31" r="26" fill="none" stroke="var(--red)" stroke-width="5"/><text x="31" y="41" text-anchor="middle" font-family="Open Sans,Arial,sans-serif" font-size="28" font-weight="700" fill="var(--red)">$</text></svg>
  <h3>Key Investment<br>Themes</h3>
  <p>Retail and consumer products sector in the GCC region is estimated at c. USD 110 bn and expected</p>
</div>
<div class="service-card" style="left:355px">
  <svg width="62" height="62" viewBox="0 0 62 62"><rect x="8" y="36" width="9" height="20" fill="var(--red)"/><rect x="21" y="28" width="9" height="28" fill="var(--red)"/><rect x="34" y="20" width="9" height="36" fill="var(--red)"/><rect x="47" y="12" width="9" height="44" fill="var(--red)"/><circle cx="20" cy="12" r="9" fill="var(--red)"/></svg>
  <h3>Investment<br>Strategy</h3>
  <p>HPC partners with global emerging brands and provides seed investment of up to USD 500,000</p>
</div>
<div class="service-card" style="left:609px">
  <svg width="62" height="62" viewBox="0 0 62 62"><circle cx="31" cy="20" r="11" fill="var(--red)"/><path d="M10 56c2-14 10-22 21-22s19 8 21 22z" fill="var(--red)"/></svg>
  <h3>Active<br>Management</h3>
  <p>HPC works along with the partner company to develop a localized operating model which caters..</p>
</div>
<div class="service-card" style="left:863px">
  <svg width="62" height="62" viewBox="0 0 62 62"><circle cx="31" cy="31" r="20" fill="var(--red)"/><circle cx="31" cy="31" r="27" fill="none" stroke="var(--red)" stroke-width="3" stroke-dasharray="6 5"/><text x="31" y="40" text-anchor="middle" font-family="Open Sans,Arial,sans-serif" font-size="24" font-weight="700" fill="#fff">$</text></svg>
  <h3>Investment<br>Monetization</h3>
  <p>HPC expects to complete up to 5 investments across retail and consumer products by 2023..</p>
</div>

<section class="why" role="img" aria-label="Upward view of glass skyscrapers">
  <svg class="why-red" width="620" height="534"><polygon points="0,0 616,0 452,534 0,534" fill="var(--red)"/></svg>
  <ul class="why-list">
    <li>Specialist Investor</li><li>Operational &amp; Business Risk</li><li>Investment Positioning</li><li>Investment Credentials</li><li>Investment Team</li><li>Management Team</li><li>Investment Pipeline</li>
  </ul>
  <div class="why-heading">WHY<br>HARBORLINE<br>CAPITAL LIMITED?</div>
</section>

<h2 class="about-title"><span class="mark"></span>About <em>Harborline Partners &amp; Co</em></h2>
<div class="about-text">
  <p>Harborline Partners &amp; Co ("HPC") is an investment and management firm providing growth capital to global emerging brands in the consumer sector which target to enter the GCC. HPC operates under commercial license 761408 and its business activities comprise investment and management across multi sectors, including retail and consumer products. The firm was incorporated in Dubai in July 2016.</p>
  <p>The firm was established by a group of reputable investors with extensive track record in private equity, M&amp;A and entrepreneurship. The firm's strength is access to capital, screening, evaluation and selection of global brands in operations management.</p>
  <p style="margin-top:22px"><span class="btn">Read More</span></p>
</div>
<div class="about-photo" role="img" aria-label="Business team reviewing a growth chart at a meeting table"></div>

<section class="stages"></section>
<h2 class="section-title" style="top:2278px"><span class="mark"></span>Our <em>Main Stages</em></h2>
<svg class="abs" style="left:0;top:2192px" width="1200" height="562">
  <g fill="none" stroke="var(--red)" stroke-width="12">
    <path d="M110 440 V358 H230"/>
    <path d="M332 362 V278 H448"/>
    <path d="M548 268 V190 H664"/>
    <path d="M764 178 V106 H880"/>
  </g>
  <g fill="var(--red)">
    <circle cx="193" cy="410" r="19"/><circle cx="415" cy="330" r="19"/><circle cx="632" cy="235" r="19"/><circle cx="852" cy="150" r="19"/>
  </g>
  <g fill="#fff" font-family="Open Sans,Arial,sans-serif" font-size="15" font-weight="700" text-anchor="middle">
    <text x="193" y="415">1</text><text x="415" y="335">2</text><text x="632" y="240">3</text><text x="852" y="155">4</text>
  </g>
</svg>
<div class="stage-label" style="left:128px;top:2628px;width:130px">Design and<br>innovation</div>
<div class="stage-label" style="left:355px;top:2552px;width:125px">Roll-out<br>growth</div>
<div class="stage-label" style="left:590px;top:2452px;width:90px">Maturity</div>
<div class="stage-label" style="left:795px;top:2370px;width:120px">Reinvention</div>
<ul class="stage-notes">
  <li>Harborline Capital is a specialist investment and management firm which provides growth capital to global emerging retail brands during the growth phase.</li>
  <li>A typical retailer/brand, during roll-out or growth phase, is well positioned to absorb financial investment and provide a cash positive and high growth value proposition due to its high ROI of c. 12%.</li>
</ul>

<h2 class="section-title" style="top:2840px"><span class="mark"></span>Latest Blog <em>News</em></h2>
<article class="post" style="left:96px">
  <div class="post-image" role="img" aria-label="Colleagues working with laptops and documents at a desk" style="background:linear-gradient(135deg,#3a3a3a,#8a8a8a 50%,#d8d8d8)"></div>
  <h4>Key Insights for Retail Sector in GCC</h4>
  <p>Retail and consumer products in GCC is estimated at USD 59 bn and expected to growth at a CAGR of 6% by 2020. Internet retailing represents only 1% as compared to developed markets where e-Commerce equals 15% to 20%.</p>
  <span class="read-more">Read More <svg width="12" height="12"><circle cx="6" cy="6" r="6" fill="var(--red)"/><path d="M5 3l3 3-3 3" stroke="#fff" stroke-width="1.6" fill="none"/></svg></span>
</article>
<article class="post" style="left:615px">
  <div class="post-image" role="img" aria-label="Hands holding a financial report with charts beside a calculator" style="background:linear-gradient(135deg,#6b97c8,#e9eef4 50%,#b9c6d3)"></div>
  <h4>Omni-Channel as Market Entry Strategy</h4>
  <p>GCC is ranked in the top 10 global growth omnichannel markets due to degree of digitization, consumer behavior, internet infrastructure and an economically active population. Omnich bric target to expand in the region.</p>
  <span class="read-more">Read More <svg width="12" height="12"><circle cx="6" cy="6" r="6" fill="var(--red)"/><path d="M5 3l3 3-3 3" stroke="#fff" stroke-width="1.6" fill="none"/></svg></span>
</article>

<section class="partners" aria-label="Partners">
  <div class="partner"></div><div class="partner"></div><div class="partner"></div><div class="partner" style="width:60px"></div><div class="partner"></div><div class="partner" style="width:60px"></div>
</section>

<footer class="site-footer">
  <div class="footer-col" style="left:96px;width:330px">
    <h5>Contact Us</h5>
    <div class="contact-line"><svg width="16" height="20" viewBox="0 0 16 20"><path d="M8 1a6 6 0 0 0-6 6c0 5 6 12 6 12s6-7 6-12a6 6 0 0 0-6-6z" fill="none" stroke="#fff" stroke-width="1.6"/><circle cx="8" cy="7" r="2" fill="#fff"/></svg><span>HARBORLINE PARTNERS &amp; CO LLC<br>Office 1807, Corniche Point Tower<br>Dubai, United Arab Emirates</span></div>
    <div class="contact-line"><svg width="16" height="16" viewBox="0 0 16 16"><path d="M3 1h3l1 4-2 1c1 2 3 4 5 5l1-2 4 1v3c0 1-1 2-2 2C7 15 1 9 1 3c0-1 1-2 2-2z" fill="none" stroke="#fff" stroke-width="1.4"/></svg><span>Phone:&nbsp; 00971 4 555 0182</span></div>
    <div class="contact-line"><svg width="18" height="14" viewBox="0 0 18 14"><rect x="1" y="1" width="16" height="12" fill="none" stroke="#fff" stroke-width="1.4"/><path d="M1 1l8 7 8-7" fill="none" stroke="#fff" stroke-width="1.4"/></svg><span>info@harborlinegroup.ae</span></div>
  </div>
  <div class="footer-col" style="left:455px">
    <h5>Quick Links</h5>
    <ul class="links"><li>Home</li><li>About Us</li><li>Our Approach</li><li>Our Portfolio</li><li>Our People</li></ul>
  </div>
  <div class="footer-col" style="left:663px">
    <h5>Other Links</h5>
    <ul class="links"><li>Privacy policy</li><li>Information</li><li>Sitemap</li><li>Contact Us</li><li>Disclaimer</li></ul>
  </div>
  <div class="footer-col newsletter" style="left:844px">
    <h5>Subscribe to our newsletter</h5>
    <p>Get our latest market notes and portfolio updates sent straight to your inbox.</p>
    <div class="field">Enter Mail..</div>
    <span class="btn">Subscribe</span>
  </div>
</footer>
<div class="copyright">© copyright 2017 Harborline Partners &amp; Co LLC. All Rights Reserved</div>

</body>
</html>
```